Post Card Design - Photo on front, details on back. Logo on both sides.

Back: See the photo of my old card. The back worked well, as it gave me lots of space to write on. The address details are still correct, but the logo has changed to Josephine Sans. Logo can be on one line or on two (if two, align it on the left).
Don't include the 'BEAUTIFUL WEDDING DRESSES...' bit.
I'd like to print this on thicker, slightly coarse paper, so don't go too small on detail.
Here are the Plume paper details: Paper Stock: Natural Uncoated
Paper Thickness: Premium
Finish: None
Front of Card: I'd like to see options for both pictures:
I think the painted image would look best with a frame in a pale shade and the logo in the frame fairly subtle.
The actual dress photo I'd like to see cropped a bit like in my mock up. You'll need to have a look at how the logo would be best placed on this. You can place it anywhere, or add a banner.
See my website for my brand's look: mirabeltoft.co.nz
Target Market(s)
Brides
Industry/Entity Type
Wedding Dresses
Contact Information for Business Card
Front: Photo and logo. Back: with details and lots of empty space. See attached photos for loose brief.
Other font styles liked:
- Josephine Sans
Requirements
Must have
- I hand-write the gown designs and price on the back of the card, so there needs to be plenty of empty space.
Nice to have
- As per brief.
Should not have
- It must look clean, romantic, modern. Timeless.

```html
<!DOCTYPE html>
<html lang="en">
<head>
<meta charset="utf-8">
<title>Mirabel Toft – Postcard</title>
<link rel="stylesheet" href="https://fonts.googleapis.com/css2?family=Josefin+Sans:wght@300;600&family=Mulish:wght@400&display=swap">
<style>
  :root {
    --backdrop: #2f2f31;
    --frame-cream: #fff5e0;
    --art-peach: #f3d3a6;
    --art-pink: #f0a3a0;
    --art-rose: #e77d8a;
    --band-cream: rgba(255, 244, 226, 0.78);
    --ink: #2e2e30;
    --card-white: #ffffff;
    --footer-grey: #d9d9d9;
    --footer-ink: #3a3a3c;
  }
  * { box-sizing: border-box; margin: 0; padding: 0; }
  html, body { width: 1200px; height: 1200px; overflow: hidden; }
  body { background: var(--backdrop); position: relative; }

  .card { position: absolute; top: 244px; height: 659px; }

  /* Front */
  .card-front { left: 40px; width: 532px; background: var(--frame-cream); }
  .front-art {
    position: absolute; left: 17px; top: 17px; right: 17px; bottom: 17px;
    background:
      radial-gradient(ellipse 38% 30% at 30% 72%, var(--art-pink) 0%, transparent 100%),
      radial-gradient(ellipse 30% 26% at 78% 30%, var(--art-rose) 0%, transparent 100%),
      radial-gradient(ellipse 28% 30% at 55% 40%, #f6ead6 0%, transparent 100%),
      radial-gradient(ellipse 35% 24% at 60% 78%, #f7e9d2 0%, transparent 100%),
      linear-gradient(180deg, #f1d3a8 0%, var(--art-peach) 100%);
  }
  .front-band {
    position: absolute; left: 17px; right: 17px; top: 282px; height: 97px;
    background: var(--band-cream);
    display: flex; justify-content: center; align-items: center;
  }
  .front-logo {
    font-family: "Josefin Sans", sans-serif; font-weight: 300;
    font-size: 43px; letter-spacing: 1.5px; color: var(--ink); line-height: 1;
    padding-top: 6px;
  }

  /* Back */
  .card-back { left: 629px; width: 535px; background: var(--card-white); }
  .back-logo {
    position: absolute; top: 22px; left: 0; right: 0; text-align: center;
    font-family: "Josefin Sans", sans-serif; font-weight: 300;
    font-size: 39px; letter-spacing: 1.4px; color: var(--ink); line-height: 1;
  }
  .back-footer {
    position: absolute; left: 0; right: 0; bottom: 0; height: 76px;
    background: var(--footer-grey);
    font-family: "Mulish", sans-serif; color: var(--footer-ink);
    display: flex; align-items: center; justify-content: center;
  }
  .footer-contacts { display: flex; gap: 11px; font-size: 11.5px; letter-spacing: 0.9px; }
  .contact-item { display: flex; align-items: center; gap: 3px; }
  .contact-icon { width: 11px; height: 11px; fill: var(--footer-ink); }
  .contact-icon.outline { fill: none; stroke: var(--footer-ink); stroke-width: 2; }
</style>
</head>
<body>
  <section class="card card-front">
    <div class="front-art" role="img" aria-label="Vintage painted illustration of a bride in a white gown and a groom in a suit, surrounded by large pink, peach and yellow painted flowers"></div>
    <div class="front-band">
      <div class="front-logo">MIRABEL TOFT</div>
    </div>
  </section>

  <section class="card card-back">
    <div class="back-logo">MIRABEL TOFT</div>
    <footer class="back-footer">
      <div class="footer-contacts">
        <span class="contact-item">
          <svg class="contact-icon" viewBox="0 0 24 24"><path d="M6.6 10.8a15.1 15.1 0 0 0 6.6 6.6l2.2-2.2a1 1 0 0 1 1-.25 11.4 11.4 0 0 0 3.6.57 1 1 0 0 1 1 1V20a1 1 0 0 1-1 1A17 17 0 0 1 3 4a1 1 0 0 1 1-1h3.5a1 1 0 0 1 1 1c0 1.25.2 2.45.57 3.57a1 1 0 0 1-.25 1z"/></svg>
          +64 9 412 5067
        </span>
        <span class="contact-item">
          <svg class="contact-icon" viewBox="0 0 24 24"><path d="M2 5h20v14H2z"/><path d="M3.5 6.5 12 13l8.5-6.5" fill="none" stroke="#d9d9d9" stroke-width="1.6"/></svg>
          mirabel@mirabeltoft.co.nz
        </span>
        <span class="contact-item">
          <svg class="contact-icon outline" viewBox="0 0 24 24"><circle cx="12" cy="12" r="10"/><ellipse cx="12" cy="12" rx="4.5" ry="10"/><path d="M2 12h20M4 6.5h16M4 17.5h16"/></svg>
          mirabeltoft.co.nz
        </span>
      </div>
    </footer>
  </section>
</body>
</html>
```